Wine label - premium, elegant & classic

We are a young husband and wife team who have worked in the wine industry for 10+ years. This year we've finally had the opportunity to make our own wine and release our own brand. Our wines are boutique and sell at a mid-premium price (we don't make a lot) so we're looking for a label design that can reflect this premium nature and mixes traditional design elements with modern reflections.

The brand is called: M&L
Updates

Project Deadline Extended
Reason: We've received some great design concepts over the past week which we would happily pay for, so we've decided to guarantee payment and extend the deadline to allow time for more designs to be sent through. A BIG thanks to all who have already submitted, your designs are still under consideration. Cheers, L.

A big thank you to all for taking the time to submit your beautiful designs to our project.  We now have the very tough job of looking over each of them and selecting only one.  We hope to come to a decision in the next day or two, so hopefully we won't keep you waiting too long!

Cheers, and thanks again

M&L.                                   

Target Market(s)

30 - 45 year old female and male wine drinkers

Industry/Entity Type

Industry

Requirements
Must have
• Can we please see two versions of the one design - one for a red wine and one for a white wine.

The front labels needs to include the following information:
1. Brand name: M&L
2. Wine varieties: Pinot Noir (red wine) and Sauvignon Blanc (white wine)
3. Vintage: 2012 for both
4. Region: Yarra Valley
5. GI: Wine of Australia (not essential to be on front label)

The back label needs to include the following:
1. The brand name: M&L
2. Variety, vintage, region and volume (the volume must be 4mm in height)
3. Room for product description - approx. 30-40 words.
4. Alcohol statement (no size restriction, pls use 12.5% ALC/VOL as example)
5. Standard drinks (no size restriction, pls use 'Approx.7.8 standard drinks' as example)
6. Sulphites statement: "Sulphites added."
7. Allergen statement: "Fined with the aid of egg and milk products and traces may remain."
8. Room for address: Approx. 20 words
9. "Wine of Australia" - no size restriction, just needs to be legible

Packaging presentation:
Pinot Noir is a red wine and Sauvignon Blanc is a white wine.
Labels for both need to be shown on premium punted burgundy bottles (pls see example: http://www.pelvornglass.com/products_services/pvg_premium_burgundy_750_ml_wine_bottle.html)
Nice to have
• We would like the design to embody the following elements:
1. Classically modern
2. Clean and simple
3. Elegance
4. Restricted use of colours (ideally just black/grey, white/buff and perhaps one other)

Some design examples of what we like:
1. http://www.fenwickhollow.com.au/sangiovese-tasting-notes/
2. http://corlunbend.com/Wines/Corlun-Bend-Vineyard/Range/2010-Corlun-Bend-Single-Vineyard-Pinot-Noir-.htm
Should not have
• Preferrably won't have any photos or drawings unless you feel there is a simple symbol or image that could be used to enhance the design.

Restricted use of colours - more muted, conservative tones.

```html
<!DOCTYPE html>
<html lang="en">
<head>
<meta charset="utf-8">
<title>M&amp;L Yarra Valley Pinot Noir 2012 – Front Label</title>
<link rel="stylesheet" href="https://fonts.googleapis.com/css2?family=Oswald:wght@300;400&family=Pinyon+Script&family=Open+Sans:wght@600&display=swap">
<style>
  :root {
    --paper: #ffffff;
    --frame: #b9bdbd;
    --region: #c9cbcb;
    --variety: #767878;
    --mark: #7f9190;
    --band: #8c8c8c;
    --band-text: #ffffff;
  }
  html, body {
    margin: 0;
    width: 1200px;
    height: 1200px;
    overflow: hidden;
    background: var(--paper);
  }
  .canvas {
    position: relative;
    width: 1200px;
    height: 1200px;
    background: var(--paper);
  }
  .label {
    position: absolute;
    left: 326px;
    top: 231px;
    width: 342px;
    height: 461px;
    transform: scale(1.6);
    transform-origin: 0 0;
    box-sizing: border-box;
    border: 1px solid var(--frame);
    background: var(--paper);
  }
  .label__strip {
    position: absolute;
    left: 137px;
    top: -1px;
    width: 68px;
    height: 294px;
    box-sizing: border-box;
    border-left: 1px solid var(--frame);
    border-right: 1px solid var(--frame);
    border-bottom: 1px solid var(--frame);
  }
  .label__brand {
    position: absolute;
    left: 150px;
    top: 102px;
    width: 40px;
    height: 170px;
    display: flex;
    flex-direction: column;
    align-items: center;
    justify-content: space-between;
    font-family: "Oswald", sans-serif;
    font-weight: 400;
    font-size: 44px;
    line-height: 1;
    color: var(--mark);
  }
  .label__region {
    position: absolute;
    left: 10px;
    top: 334px;
    margin: 0;
    font-family: "Oswald", sans-serif;
    font-weight: 300;
    font-size: 22px;
    letter-spacing: 5.2px;
    line-height: 1;
    color: var(--region);
  }
  .label__variety {
    position: absolute;
    left: 157px;
    top: 356px;
    margin: 0;
    font-family: "Pinyon Script", cursive;
    font-size: 22px;
    line-height: 1;
    color: var(--variety);
  }
  .label__vintage {
    position: absolute;
    left: -1px;
    right: -1px;
    bottom: -1px;
    height: 28px;
    background: var(--band);
    display: flex;
    align-items: center;
    justify-content: center;
    font-family: "Open Sans", sans-serif;
    font-weight: 600;
    font-size: 13px;
    letter-spacing: 3px;
    color: var(--band-text);
  }
</style>
</head>
<body>
  <main class="canvas">
    <section class="label" aria-label="Front wine label">
      <div class="label__strip"></div>
      <div class="label__brand" aria-label="M&amp;L">
        <span>M</span><span>&amp;</span><span>L</span>
      </div>
      <h1 class="label__region">YARRA VALLEY</h1>
      <h2 class="label__variety">Pinot Noir</h2>
      <div class="label__vintage">2012</div>
    </section>
  </main>
</body>
</html>
```